Website Redesign for Brightvale Forge

We are looking for a high-end Minimalist Design That will give potential customers the feel that they are purchasing a hand-crafted reproduction of an actual historical medieval sword. The tone or feel should like a luxury sword manufacturer.
Perhaps having a darker background with logo/text that pops more with a white glow.

Target Market(s)

Historical "efficinato" - educated history buffs interested in high end swords & armors, with a available capital for such a hobby.

Number of Pages Required

3 page

Font styles to use
Serif

Colors
1b1b1b
000000
e6e6e6
c9c9c9

Requirements
Must have
• -cart page
• -home page
• -1 product page
Nice to have
• -large images
• - Garamon or Centaur font
• - Our logo is in Trojan Pro
Should not have
• -no excessive use of colors
• -no medieval / gothic fonts

```html
<!DOCTYPE html>
<html lang="en">
<head>
<meta charset="utf-8">
<title>Brightvale Forge — Medieval Swords</title>
<link rel="stylesheet" href="https://fonts.googleapis.com/css2?family=Cinzel:wght@400;700&family=Open+Sans:wght@400;600&display=swap">
<style>
:root{
  --ink:#000000;
  --base:#1b1b1b;
  --panel:#141414;
  --deep:#0d0d0d;
  --light:#e6e6e6;
  --mid:#c9c9c9;
  --muted:#8a8a8a;
  --line:#333333;
  --serif:'Cinzel', Georgia, serif;
  --sans:'Open Sans', Arial, sans-serif;
}
*{margin:0;padding:0;box-sizing:border-box}
html,body{width:690px;height:1200px;overflow:hidden}
body{background:var(--base);color:var(--light);font-family:var(--sans);position:relative}
.abs{position:absolute}

/* header */
.site-header{left:0;top:0;width:690px;height:69px;background:var(--ink)}
.brand{left:24px;top:14px;display:flex;align-items:center;gap:10px}
.brand-mark{width:34px;height:34px;background:var(--light)}
.brand-name{font-family:var(--serif);font-weight:700;font-size:15px;line-height:16px;color:var(--light);letter-spacing:.5px}
.header-tools{right:22px;top:26px;display:flex;align-items:center;gap:8px;font-size:10px;color:var(--mid)}
.header-tools svg{display:block}
.social{display:flex;gap:4px}
.social span{width:15px;height:15px;background:var(--mid);border-radius:2px;display:block}

/* nav */
.main-nav{left:0;top:69px;width:690px;height:28px;background:linear-gradient(#2e2e2e,#1f1f1f);border-top:1px solid #3a3a3a;display:flex}
.main-nav a{flex:auto;font-family:var(--serif);font-size:10px;color:var(--mid);text-decoration:none;display:flex;align-items:center;justify-content:center;border-right:1px solid #111}
.main-nav a.is-active{background:linear-gradient(#4a4a4a,#333);color:#fff}

/* hero */
.hero{left:0;top:97px;width:690px;height:317px;background:linear-gradient(120deg,#151515 0%,#3c3c3c 45%,#7a7a7a 62%,#2a2a2a 80%,#111 100%)}
.hero-title{left:32px;top:323px;font-family:var(--serif);font-size:34px;color:#fff;letter-spacing:1px;text-shadow:0 0 10px rgba(255,255,255,.25)}
.hero-sub{left:34px;top:366px;font-family:var(--serif);font-size:10px;color:var(--mid);letter-spacing:.5px}
.slider-arrows{display:flex;gap:3px}
.slider-arrows span{width:18px;height:18px;background:rgba(0,0,0,.6);display:flex;align-items:center;justify-content:center}

/* about */
.about{left:0;top:414px;width:690px;height:222px;background:var(--panel)}
.video{left:46px;top:448px;width:230px;height:150px;background:linear-gradient(160deg,#6b6b6b,#3a3a3a 55%,#222)}
.play{left:141px;top:503px;width:40px;height:40px;border-radius:50%;background:rgba(0,0,0,.65);border:2px solid var(--light)}
.about-icon{left:296px;top:450px;width:30px;height:30px;background:var(--light)}
.about-title{left:336px;top:446px;font-family:var(--serif);font-size:14px;line-height:17px;color:#fff}
.about-copy{left:296px;top:492px;width:350px;font-size:7px;line-height:10px;color:var(--muted)}
.about-copy p{margin-bottom:6px}
.about-btn{left:296px;top:580px;font-family:var(--serif);font-size:7px;color:var(--light);background:#2c2c2c;border:1px solid #444;padding:4px 8px}

/* recent */
.recent{left:0;top:636px;width:690px;height:220px;background:var(--deep)}
.section-title{font-family:var(--serif);font-size:18px;color:#fff}
.recent-title{left:46px;top:656px}
.recent-arrows{right:46px;top:660px;display:flex;gap:6px}
.product-row{left:46px;top:686px;display:flex;gap:12px}
.product{width:140px}
.product-image{width:140px;height:108px}
.product-name{font-family:var(--serif);font-size:8px;color:var(--mid);text-align:center;margin-top:8px;white-space:nowrap}
.product-name::before{content:"";display:inline-block;width:10px;height:1px;background:var(--muted);vertical-align:middle;margin-right:4px}

/* blog */
.blog-title{left:46px;top:874px;font-size:14px}
.post{top:905px;width:290px;display:flex;gap:10px}
.post-image{width:74px;height:80px;flex:none}
.post-body h3{font-family:var(--serif);font-weight:400;font-size:9px;color:#fff}
.post-date{font-size:6px;color:var(--muted);margin:2px 0 4px}
.post-body p{font-size:6px;line-height:9px;color:var(--muted)}
.post-more{font-size:6px;color:var(--mid);margin-top:3px}

/* footer */
.site-footer{left:0;top:1030px;width:690px;height:146px;background:var(--panel);border-top:1px solid var(--line)}
.footer-brand{left:46px;top:1072px;display:flex;align-items:center;gap:10px}
.footer-brand .brand-name{font-size:17px;line-height:19px}
.footer-col{top:1052px}
.footer-col h4{font-family:var(--serif);font-weight:400;font-size:9px;color:#fff;margin-bottom:6px}
.footer-col li{list-style:none;font-size:6.5px;line-height:10px;color:var(--muted)}
.footer-col p{font-size:6.5px;line-height:10px;color:var(--muted)}
.subscribe{display:flex;margin-top:6px}
.subscribe span{display:block;height:14px}
.subscribe .field{width:86px;background:#2a2a2a;border:1px solid #3c3c3c}
.subscribe .go{width:30px;background:#3a3a3a;font-size:6px;color:var(--light);text-align:center;line-height:14px}
.footer-social{display:flex;gap:6px;margin-top:10px}
.footer-social span{width:16px;height:16px;border-radius:50%;border:1px solid var(--muted);display:block}
.copyright{left:0;top:1176px;width:690px;height:24px;background:var(--ink);font-size:7px;color:var(--muted);text-align:center;line-height:24px}
</style>
</head>
<body>

<header class="site-header abs">
  <div class="brand abs">
    <span class="brand-mark"></span>
    <span class="brand-name">BRIGHTVALE<br>FORGE</span>
  </div>
  <div class="header-tools abs">
    <svg width="10" height="10" viewBox="0 0 10 10"><path d="M2 1l2 2-1 1.5c.6 1.2 1.3 1.9 2.5 2.5L7 6l2 2-1.5 1.5C4.5 9 1 5.5.5 2.5z" fill="#c9c9c9"/></svg>
    <span>1.800.555.0142</span>
    <svg width="12" height="10" viewBox="0 0 12 10"><path d="M0 1h2l1.5 6h6.5l1.5-4.5H3" fill="none" stroke="#c9c9c9" stroke-width="1.2"/><circle cx="4.5" cy="9" r="1" fill="#c9c9c9"/><circle cx="9" cy="9" r="1" fill="#c9c9c9"/></svg>
    <span>CART : 0</span>
    <div class="social"><span></span><span></span><span></span><span></span></div>
  </div>
</header>

<nav class="main-nav abs">
  <a class="is-active">MEDIEVAL SWORDS</a>
  <a>ARMORS</a>
  <a>DAGGERS</a>
  <a>AXES</a>
  <a>VIKING JEWELRY</a>
  <a>BLOG</a>
  <a>SALE ITEMS</a>
</nav>

<section class="hero abs" role="img" aria-label="Close-up of an ornate engraved sword hilt and blade"></section>
<h1 class="hero-title abs">ELITE SERIES</h1>
<p class="hero-sub abs">NEQUE PORRO QUISQUAM EST QUI DOLOREM</p>
<div class="slider-arrows abs" style="left:622px;top:384px">
  <span><svg width="6" height="8" viewBox="0 0 6 8"><path d="M5 0L1 4l4 4" fill="none" stroke="#e6e6e6"/></svg></span>
  <span><svg width="6" height="8" viewBox="0 0 6 8"><path d="M1 0l4 4-4 4" fill="none" stroke="#e6e6e6"/></svg></span>
</div>

<section class="about abs"></section>
<div class="video abs" role="img" aria-label="Video still of a sword being forged in a workshop"></div>
<div class="play abs"><svg width="36" height="36" viewBox="0 0 36 36"><path d="M14 11l11 7-11 7z" fill="#e6e6e6"/></svg></div>
<span class="about-icon abs"></span>
<h2 class="about-title abs">MEDIEVAL SWORDS, BATTLE READY<br>SWORDS,DAGGERS AND ARMORS</h2>
<div class="about-copy abs">
  <p>Brightvale Forge crafts fully functional swords, daggers and medieval weapons, each one individually hand forged from high carbon steel and tempered by our smiths. Every blade is built for balance, strength and lasting edge, and is shaped after pieces held in museum collections across Europe. Our aim is to honour the craft of the period in every detail we make.</p>
  <p>A commitment that has earned us a reputation for crafting some of the finest battle ready swords on the market. Our line of medieval swords is also featured in films, collections and study groups.</p>
</div>
<span class="about-btn abs">READ MORE</span>

<section class="recent abs"></section>
<h2 class="section-title recent-title abs">MOST RECENT</h2>
<div class="recent-arrows abs">
  <svg width="7" height="10" viewBox="0 0 7 10"><path d="M6 0L1 5l5 5" fill="none" stroke="#e6e6e6" stroke-width="1.5"/></svg>
  <svg width="7" height="10" viewBox="0 0 7 10"><path d="M1 0l5 5-5 5" fill="none" stroke="#e6e6e6" stroke-width="1.5"/></svg>
</div>
<div class="product-row abs">
  <div class="product"><div class="product-image" role="img" aria-label="Long sword resting diagonally" style="background:linear-gradient(135deg,#3a3a3a,#8c8c8c 50%,#2a2a2a)"></div><p class="product-name">NIGHTWARDEN SWORD</p></div>
  <div class="product"><div class="product-image" role="img" aria-label="Sword blade on pale background" style="background:linear-gradient(135deg,#d9d9d9,#a6a6a6 60%,#777)"></div><p class="product-name">THE ALDRIC SWORD</p></div>
  <div class="product"><div class="product-image" role="img" aria-label="Swordsman in armor holding a blade" style="background:linear-gradient(160deg,#4a4a4a,#1c1c1c)"></div><p class="product-name">NIGHTWARDEN SWORD</p></div>
  <div class="product"><div class="product-image" role="img" aria-label="Sword hilt detail in soft light" style="background:linear-gradient(135deg,#e0e0e0,#9a9a9a 55%,#555)"></div><p class="product-name">THE ALDRIC SWORD</p></div>
</div>

<h2 class="section-title blog-title abs">LATEST BLOG</h2>
<article class="post abs" style="left:46px">
  <div class="post-image" role="img" aria-label="Smith working at the forge" style="background:linear-gradient(160deg,#6a6a6a,#2c2c2c)"></div>
  <div class="post-body">
    <h3>SIMPLY DUMMY TEXT</h3>
    <p class="post-date">12 July 2014</p>
    <p>Notes from the forge floor this month, where our smiths shaped a new run of blades and tested each one for edge, balance and temper before it left the shop.</p>
    <p class="post-more">Read More »</p>
  </div>
</article>
<article class="post abs" style="left:355px">
  <div class="post-image" role="img" aria-label="Craftsman inspecting a finished sword" style="background:linear-gradient(160deg,#7a7a7a,#333)"></div>
  <div class="post-body">
    <h3>SIMPLY DUMMY TEXT</h3>
    <p class="post-date">08 July 2014</p>
    <p>A look at how a historical hilt is studied, measured and rebuilt by hand, from first sketch to final polish, so the finished piece stays true to the period.</p>
    <p class="post-more">Read More »</p>
  </div>
</article>

<footer class="site-footer abs"></footer>
<div class="footer-brand abs">
  <span class="brand-mark" style="width:38px;height:38px"></span>
  <span class="brand-name">BRIGHTVALE<br>FORGE</span>
</div>
<div class="footer-col abs" style="left:262px">
  <h4>PRODUCTS</h4>
  <ul><li>» Medieval Swords</li><li>» Elite Series</li><li>» Medieval Daggers</li><li>» Medieval Armor</li><li>» Accessories</li></ul>
</div>
<div class="footer-col abs" style="left:400px">
  <h4>GET IN TOUCH</h4>
  <p>Address : 14 Anvil Lane<br>Vale Hollow<br>Phone : 1.800.555.0142<br>Email : hello@brightvaleforge.com</p>
</div>
<div class="footer-col abs" style="left:530px">
  <h4>NEWSLETTER</h4>
  <p>Get news and offers straight<br>to your inbox.</p>
  <div class="subscribe"><span class="field"></span><span class="go">Submit</span></div>
  <div class="footer-social"><span></span><span></span><span></span></div>
</div>
<div class="copyright abs">Copyright © 2014. All Rights Reserved.</div>

</body>
</html>
```